Homepage Website Design for luxury picnic company

We need a homepage designed for a luxury picnic business to match our updated branding/logo which we're currently completing on ArtHivePro with another competition. Please see attached logo/colour example to use for now.

PLEASE NOTE: We are only after graphic design concepts as part of this competition. I will get another developer to actually code the website.

It is important that this website is very elegant/luxurious and stands out from a visual perspective. The images really need to match the content/sections also. The new branding colours are silver with a dark background. Please create the new website homepage to match these colours/branding.

Please create as many concepts as possible and then I will provide feedback from there

The website content including sections is here https://papers.quillnest.net/doc/7hRtK2mWqPz9LbXv4nYcJ8eFgTs3uAd6Vk1oNwEiQy/view?mode=shared

Images to use are located here https://vault.boxmerile.net/store/folders/8KmWpT3r-ZxQa5Hn92VbLcYeRduf?mode=shared and there is also lots of videos at this link which you can screenshot images out of if needed https://www.filetrunko.net/sh/k728vrum3wdx2h/QQTrfm7LkWn5EaZ9J4hvdPcXy?get=0

Any questions please contact me

```html
<!DOCTYPE html>
<html lang="en">
<head>
<meta charset="utf-8">
<title>Ridgeline Picnics — Luxury picnics at breathtaking locations</title>
<link href="https://fonts.googleapis.com/css2?family=Montserrat:wght@400;500;600;700&display=swap" rel="stylesheet">
<style>
:root{
  --night:#0c0f1e;
  --night-deep:#090b17;
  --wine:#7a1b3d;
  --wine-footer:#6b1634;
  --white:#ffffff;
  --ink:#14141c;
  --muted:#3a3a44;
  --field:#7b7b86;
  --badge:#1ba3dc;
}
*{box-sizing:border-box;margin:0;padding:0}
html,body{width:1200px;height:4195px;overflow:hidden}
body{background:var(--night);font-family:'Montserrat',sans-serif;color:var(--white);position:relative}
.abs{position:absolute}
.photo{position:absolute}
.center{text-align:center}

/* header */
.site-header{left:0;top:0;width:1200px;height:65px;background:var(--night-deep)}
.brand{left:112px;top:14px;display:flex;align-items:center;gap:8px;font-weight:600;font-size:17px;color:var(--white)}
.brand-dot{width:30px;height:30px;border:2px solid var(--white);border-radius:50%}
.menu-toggle{left:1050px;top:22px;width:38px}
.menu-toggle span{display:block;height:4px;background:var(--white);border-radius:2px;margin-bottom:6px}

/* hero */
.hero{left:0;top:65px;width:1200px;height:599px;background:linear-gradient(180deg,#4c5660 0%,#6b5a44 35%,#5a3a2e 65%,#3b2a2c 100%)}
.hero-title{left:0;top:228px;width:1200px;font-size:55px;font-weight:700;line-height:51px;letter-spacing:1px;text-shadow:0 2px 6px rgba(0,0,0,.35)}
.hero-sub{left:0;top:393px;width:1200px;font-size:27px;font-weight:500;letter-spacing:.5px}
.btn{background:var(--wine);color:var(--white);font-weight:600;display:flex;align-items:center;justify-content:center;border-radius:6px}
.hero-btn{left:492px;top:443px;width:218px;height:36px;font-size:15px;letter-spacing:.5px}
.safe-badge{border-radius:50%;background:var(--badge);border:4px solid var(--white)}
.hero-badge{left:998px;top:536px;width:88px;height:88px}

/* features */
.feature-img{top:708px;width:251px;height:168px;border-radius:12px}
.feature-title{top:894px;width:251px;font-size:20px;font-weight:700;letter-spacing:1px}
.feature-text{top:930px;width:251px;font-size:11.5px;line-height:15px;padding:0 12px}

/* video */
.video{left:0;top:1123px;width:1200px;height:419px;background:linear-gradient(90deg,#8a4a1e 0%,#a8612a 40%,#5a5a5c 70%,#3b4656 100%)}
.video-title{left:0;top:1204px;width:1200px;font-size:19px;font-weight:600;line-height:23px;letter-spacing:.5px}
.play{left:542px;top:1326px}

/* pricing */
.section-title{left:0;width:1200px;font-size:30px;font-weight:700;letter-spacing:1px}
.card{background:var(--white);color:var(--ink);border-radius:10px}
.price-card{top:1646px;width:249px;height:291px}
.price-name{position:absolute;top:14px;left:0;width:100%;font-size:21px;font-weight:600}
.price-amount{position:absolute;top:44px;left:0;width:100%;font-size:15px;font-weight:500}
.price-list{position:absolute;top:70px;left:10px;right:8px;font-size:10.5px;line-height:15px;list-style:none;color:var(--muted)}
.price-list b{color:var(--ink)}
.order-btn{position:absolute;left:82px;top:247px;width:85px;height:18px;font-size:11px;border-radius:3px}
.plans-title{left:0;top:1972px;width:1172px;font-size:20px;font-weight:700;letter-spacing:.5px}
.plans-text{left:330px;top:2014px;width:520px;font-size:12.5px;line-height:15.5px}
.plans-text p+p{margin-top:15px}

/* steps */
.steps{left:0;top:2219px;width:1200px;height:435px;background:linear-gradient(180deg,#7a8898 0%,#95a2ae 35%,#4e5d6c 65%,#2a3444 100%)}
.steps-title{left:0;top:2254px;width:1200px;font-size:20px;font-weight:600;letter-spacing:.5px}
.step-card{top:2300px;width:249px;height:207px}
.step-num{position:absolute;top:14px;left:0;width:100%;font-size:30px;font-weight:700}
.step-text{position:absolute;top:70px;left:12px;right:12px;font-size:11px;line-height:15px;color:var(--muted)}
.steps-btn{left:433px;top:2551px;width:329px;height:38px;font-size:15px;letter-spacing:.5px}

/* spots */
.spot{top:2746px;width:384px;height:258px;border-radius:10px}
.spot-name{top:2833px;width:384px;font-size:16px;font-weight:700}
.spot-btn{top:2868px;width:114px;height:18px;font-size:10px;border-radius:4px}

/* testimonials */
.quote-card{top:3096px;width:249px;height:205px}
.avatar{position:absolute;left:96px;top:16px;width:56px;height:56px;border-radius:50%;background:#4a4a52}
.quote-text{position:absolute;top:92px;left:30px;right:30px;font-size:10.5px;line-height:13px;color:var(--muted)}
.quote-name{position:absolute;top:150px;left:0;width:100%;font-size:10.5px;font-weight:700}

/* covid */
.covid-title{left:0;top:3338px;width:1200px;font-size:30px;font-weight:700}
.covid-badge{top:3357px;width:116px;height:116px}
.covid-text{left:405px;top:3396px;width:390px;font-size:12.5px;line-height:14.5px}

/* contact */
.contact{left:275px;top:3569px;width:650px;height:332px;border-radius:16px}
.contact-title{position:absolute;top:34px;left:0;width:100%;font-size:20px;font-weight:700}
.field-label{position:absolute;font-size:11px;color:var(--ink)}
.field{position:absolute;width:184px;height:24px;border:1.5px solid var(--field);border-radius:7px}
.message{position:absolute;left:399px;top:99px;width:182px;height:125px;border:1.5px solid var(--field);border-radius:6px}
.send-btn{position:absolute;left:399px;top:241px;width:83px;height:19px;font-size:11px;border-radius:4px}

/* footer */
.site-footer{left:0;top:3986px;width:1200px;height:209px;background:var(--wine-footer)}
.footer-title{left:342px;top:4020px;font-size:20px;font-weight:700}
.footer-lines{left:342px;top:4056px;font-size:11px;line-height:19.5px}
.footer-legal{left:674px;top:4053px;font-size:11px}
.copyright{left:0;top:4154px;width:1200px;font-size:11px}
</style>
</head>
<body>

<header class="abs site-header">
  <div class="abs brand"><span class="brand-dot"></span>Ridgeline Picnics</div>
  <div class="abs menu-toggle" aria-label="Menu"><span></span><span></span><span></span></div>
</header>

<section>
  <div class="photo hero" role="img" aria-label="Couple sharing wine at a luxury picnic set with cushions and flowers on a mountain cliff edge"></div>
  <h1 class="abs hero-title center">SHARE AN<br>UNFORGETTABLE<br>MOMENT</h1>
  <p class="abs hero-sub center">Luxury picnics at breathtaking locations</p>
  <div class="abs btn hero-btn">BOOK YOUR PICNIC</div>
  <div class="abs safe-badge hero-badge" role="img" aria-label="Safety certification badge"></div>
</section>

<section>
  <div class="photo feature-img" style="left:140px;background:linear-gradient(180deg,#5d6570,#3a4350 60%,#252c38)" role="img" aria-label="Couple embracing at a mountain lookout"></div>
  <div class="photo feature-img" style="left:474px;background:linear-gradient(180deg,#4a5866,#3c4450 55%,#6a4a48)" role="img" aria-label="Woman relaxing on picnic cushions above a valley"></div>
  <div class="photo feature-img" style="left:806px;background:linear-gradient(180deg,#8c9298,#b8b4ae 50%,#5a2a2a)" role="img" aria-label="Champagne bottles and glasses with a grazing platter"></div>
  <h2 class="abs feature-title center" style="left:140px">BLISS</h2>
  <h2 class="abs feature-title center" style="left:474px">UNWIND</h2>
  <h2 class="abs feature-title center" style="left:806px">INDULGE</h2>
  <p class="abs feature-text center" style="left:140px">We enable you to enjoy true quality time with your partner, friends or family. We do this by creating the perfect atmosphere to celebrate a special moment in your life or to simply spoil yourself!</p>
  <p class="abs feature-text center" style="left:474px">Let us do everything for you so you can enjoy a stress free experience. You will also discover the Blue Mountains like you never have before! Each of our picnic spots have absolutely stunning views and are also very quiet.</p>
  <p class="abs feature-text center" style="left:806px">Our delicious picnics will have your mouth watering! You can design your own picnic by choosing from our extensive menu along with your favourite alcoholic &amp; non-alcoholic beverages. We cater for all dietary requirements and also have a BYO option.</p>
</section>

<section>
  <div class="photo video" role="img" aria-label="Sandstone rock pillars glowing at sunset above a misty valley"></div>
  <h2 class="abs video-title center">WATCH THIS SHORT VIDEO<br>FOR A QUICK OVERVIEW ON OUR PICNICS</h2>
  <svg class="abs play" width="116" height="116" viewBox="0 0 116 116" aria-label="Play video">
    <circle cx="58" cy="58" r="53" fill="none" stroke="#0c0f1e" stroke-width="7"/>
    <polygon points="44,34 44,82 84,58" fill="#0c0f1e"/>
  </svg>
</section>

<section>
  <h2 class="abs section-title center" style="top:1573px">PRICING</h2>

  <div class="abs card price-card" style="left:208px">
    <h3 class="price-name center">BYO Picnic</h3>
    <p class="price-amount center">$200 + GST</p>
    <ol class="price-list">
      <li><b>1.</b> Hire transport and setup of picnic equipment</li>
      <li><b>2.</b> Directions to 'secret' location</li>
      <li><b>3.</b> 2 hour picnic</li>
      <li><b>4.</b> Cleaning and pack up</li>
      <li><b>5.</b> Still or sparkling water cooled on ice with glassware</li>
      <li><b>6.</b> BYO additional food &amp; beverages</li>
    </ol>
    <div class="btn order-btn">Order</div>
  </div>

  <div class="abs card price-card" style="left:475px">
    <h3 class="price-name center">Gourmet Picnic</h3>
    <p class="price-amount center">$350 + GST</p>
    <ol class="price-list">
      <li><b>1.</b> Everything in the BYO picnic</li>
      <li><b>2.</b> Design your own gourmet grazing platter</li>
      <li><b>3.</b> Choose 2 types of complimentary beverages</li>
      <li><b>4.</b> Delivery of the food and beverages to the picnic spot</li>
      <li><b>5.</b> Matching glassware and cutlery</li>
    </ol>
    <div class="btn order-btn">Order</div>
  </div>

  <div class="abs card price-card" style="left:742px">
    <h3 class="price-name center">Proposal Picnic</h3>
    <p class="price-amount center">$100 + GST</p>
    <ol class="price-list">
      <li><b>1.</b> 1 on 1 VIP treatment</li>
      <li><b>2.</b> Suggestions for accommodation, activites Restaurants</li>
      <li><b>3.</b> Assistance with any requests</li>
      <li><b>4.</b> Directions to location prior to the picnic</li>
      <li><b>5.</b> Help with organising photography</li>
      <li><b>6.</b> Anything else needed for a successful proposal!</li>
    </ol>
    <div class="btn order-btn">Order</div>
  </div>

  <h2 class="abs plans-title center">PAYMENT PLANS AVAILABLE</h2>
  <div class="abs plans-text center">
    <p>To secure your booking, all we need is a $100 + GST deposit. We offer custom payment plans at no extra cost. Once we receive your deposit we will be in touch to organise the best arrangements with you and just need you to have paid in full prior to the picnic.</p>
    <p>If you prefer, you can still pay upfront to save the extra mucking around with a payment plan but it makes no difference from our end so please do whatever is best for you.</p>
  </div>
</section>

<section>
  <div class="photo steps" role="img" aria-label="Cloudy sky over a wide mountain valley"></div>
  <h2 class="abs steps-title center">ORGANISING YOUR PICNIC IS AS EASY AS</h2>
  <div class="abs card step-card" style="left:208px">
    <p class="step-num center">1</p>
    <p class="step-text center">You can see the locations we offer and each of their available dates and times via our website. When you're ready you can book a picnic by either paying in full or putting down a deposit with payment plan options available at no extra cost.</p>
  </div>
  <div class="abs card step-card" style="left:475px">
    <p class="step-num center">2</p>
    <p class="step-text center">We then email you all the important information in the lead up to your picnic. You can also select your food, beverages and chalkboard message quickly and easily via our website.</p>
  </div>
  <div class="abs card step-card" style="left:742px">
    <p class="step-num center">3</p>
    <p class="step-text center">Discover your stunning picnic spot where your picnic setting will be setup waiting for you. We say a quick hello before leaving you to enjoy the experience. We provide your choice of still or sparkling water on ice at every picnic.</p>
  </div>
  <div class="abs btn steps-btn">BOOK YOUR PICNIC</div>
</section>

<section>
  <h2 class="abs section-title center" style="top:2688px">PICNIC SPOTS</h2>
  <div class="photo spot" style="left:158px;background:linear-gradient(180deg,#6a747e,#4e5660 50%,#3a2a2c)" role="img" aria-label="Bottles and glasses set out beneath trees at a clifftop lookout"></div>
  <div class="photo spot" style="left:656px;background:linear-gradient(180deg,#6c7684,#4a5462 45%,#6a2a34)" role="img" aria-label="Picnic cushions and basket on a rocky ledge above the valley"></div>
  <p class="abs spot-name center" style="left:158px">Wentworth Falls Picnic Spot</p>
  <p class="abs spot-name center" style="left:656px">Katoomba Picnic Spot</p>
  <div class="abs btn spot-btn" style="left:293px">More Details</div>
  <div class="abs btn spot-btn" style="left:791px">More Details</div>
</section>

<section>
  <h2 class="abs section-title center" style="top:3038px">TESTIMONIAL</h2>
  <div class="abs card quote-card" style="left:342px">
    <div class="avatar" role="img" aria-label="Customer portrait"></div>
    <p class="quote-text center">dolor sit amet, consectetur adipisicing elit, sed do eiusmod tempor incididunt ut labore et dolore magna aliqua.</p>
    <p class="quote-name center">Marcus L.T</p>
  </div>
  <div class="abs card quote-card" style="left:609px">
    <div class="avatar" role="img" aria-label="Customer portrait"></div>
    <p class="quote-text center">dolor sit amet, consectetur adipisicing elit, sed do eiusmod tempor incididunt ut labore et dolore magna aliqua.</p>
    <p class="quote-name center">Oliver K.R</p>
  </div>
</section>

<section>
  <h2 class="abs covid-title center">We’re COVID Safe</h2>
  <div class="abs safe-badge covid-badge" style="left:276px" role="img" aria-label="Safety certification badge"></div>
  <div class="abs safe-badge covid-badge" style="left:808px" role="img" aria-label="Safety certification badge"></div>
  <p class="abs covid-text center">We are very conscious of everyone's health and well being during these unprecedented times. You can have confidence knowing we're a registered COVID safe business with the NSW Government. We follow all health protocols when setting up and preparing our picnics. If you want to know any further details or have any requests please just reach out.</p>
</section>

<section class="abs card contact">
  <h2 class="contact-title center">contact us</h2>
  <span class="field-label" style="left:65px;top:80px">First Name</span>
  <span class="field" style="left:65px;top:99px"></span>
  <span class="field-label" style="left:65px;top:139px">Last Name</span>
  <span class="field" style="left:65px;top:158px"></span>
  <span class="field-label" style="left:65px;top:197px">Email</span>
  <span class="field" style="left:65px;top:216px"></span>
  <span class="field-label" style="left:65px;top:256px">Phone Number</span>
  <span class="field" style="left:65px;top:275px"></span>
  <span class="field-label" style="left:399px;top:80px">Message</span>
  <span class="message"></span>
  <span class="btn send-btn">Send</span>
</section>

<footer class="abs site-footer"></footer>
<h2 class="abs footer-title">Contact Us</h2>
<p class="abs footer-lines">PO Box 1187 FERNVALE NSW 2790<br>02 5550 1942<br>hello@ridgelinepicnics.example</p>
<p class="abs footer-legal">privacy policy/terms and conditions</p>
<p class="abs copyright center">copyright 2020</p>

</body>
</html>
```